Modern, sales-driven landing page with video for a photovoltaic configurator

Please create a modern landing page for a photovoltaic configurator where users can select a photovoltaic system, including installation, without entering any personal data. Users can assemble a complete package from our product portfolio and receive a realistic yield and profitability calculation, as well as a complete offer including installation. The landing page should be promoted under the Lunavolt brand (Your Lunavolt Photovoltaic Configurator...). The landing page will be hosted on its own domain: www.lunavolt-beispiel.de. When submitting an inquiry, users will be redirected to our main website: www.falke-energieplan-beispiel.de. Text and design suggestions are attached. It is important that both the Lunavolt and Falke EnergiePlan logos are included. Logos are also attached. Various certificates and seals are also included.
Rankora star ratings and 2-3 customer reviews should be visible. The image should show a tablet with a configurator. Preview images of the configurator and the results (offer, profitability calculation) should be included.

Target Market(s)

homeowners

Font styles to use
Other font styles liked:
• Poppins Bold, Inter

Requirements
Nice to have
• The page should be dark and modern.

```html
<!DOCTYPE html>
<html lang="en">
<head>
<meta charset="utf-8">
<title>Lunavolt – PV-Konfigurator</title>
<link href="https://fonts.googleapis.com/css2?family=Poppins:wght@400;500;600;700&family=Inter:wght@400;500;600&display=swap" rel="stylesheet">
<style>
:root{
  --bg:#0c1120;
  --bg-2:#10172a;
  --card:#131a2c;
  --card-2:#182036;
  --line:#232c45;
  --text:#ffffff;
  --muted:#8f98b0;
  --orange:#f7a21b;
  --orange-2:#f2840c;
}
*{box-sizing:border-box;margin:0;padding:0}
html,body{width:1200px;height:5172px;overflow:hidden;background:var(--bg);color:var(--text);font-family:Inter,sans-serif}
h1,h2,h3,.brand,.btn{font-family:Poppins,sans-serif}
.page{position:relative;width:1200px;height:5172px}
.abs{position:absolute}
.eyebrow{font-family:Poppins,sans-serif;font-size:9px;font-weight:600;letter-spacing:1.2px;color:var(--orange);text-transform:uppercase}
.center{text-align:center;left:0;width:1200px}
h2{font-size:31px;font-weight:600;line-height:1.12}
.sub{font-size:11px;color:var(--muted);line-height:1.6}
.accent{color:var(--orange)}
.btn{display:inline-flex;align-items:center;gap:8px;border-radius:20px;font-size:10px;font-weight:600;height:30px;padding:0 18px;color:#1a1204;background:linear-gradient(90deg,var(--orange),var(--orange-2));box-shadow:0 6px 20px rgba(247,150,20,.35)}
.btn.ghost{background:#182036;color:#fff;box-shadow:none}
.card{position:absolute;background:var(--card);border:1px solid var(--line);border-radius:8px}
.icon{width:28px;height:28px;border-radius:6px;background:#2a2412;border:1px solid #4a3a16;display:flex;align-items:center;justify-content:center}
.card h3{font-size:12.5px;font-weight:600;margin-top:14px}
.card p{font-size:9.5px;color:var(--muted);line-height:1.55;margin-top:6px}

/* hero */
.hero{position:absolute;left:0;top:0;width:1200px;height:640px;overflow:hidden;background:#0d1324}
.hero-photo{position:absolute;left:380px;top:0;width:820px;height:640px;background:radial-gradient(ellipse at 85% 8%,#ffcf6a 0,#d98a2a 6%,#4b3a2f 22%,rgba(20,26,44,0) 50%),radial-gradient(ellipse at 62% 55%,#3a3f4c 0,#222938 35%,rgba(13,19,36,0) 70%),linear-gradient(90deg,#0d1324 0,rgba(13,19,36,.2) 30%,#1a1f2c 100%)}
.logo{display:flex;flex-direction:column;align-items:center;gap:8px}
.logo .mark{width:58px;height:58px;border-radius:50%;border:3px solid #fff}
.logo .brand{font-size:18px;font-weight:600;letter-spacing:1.5px}
.hero h1{font-size:38px;font-weight:600;line-height:1.17;width:450px}
.checks li{list-style:none;font-size:11px;font-weight:600;display:flex;align-items:center;gap:7px;margin-bottom:11px}
.dot{width:12px;height:12px;border-radius:50%;background:var(--orange);display:inline-flex;align-items:center;justify-content:center;flex:none}
.btn-hero{height:40px;padding:0 6px 0 18px;font-size:12px;border-radius:22px;gap:14px}
.btn-hero .circ{width:30px;height:30px;border-radius:50%;background:#fff;display:flex;align-items:center;justify-content:center}
.partner{font-family:Poppins,sans-serif;font-size:15px;font-weight:700;color:#4fb4ff;line-height:1}

/* photos */
.photo{position:absolute;border-radius:10px}
.stat-box{position:absolute;background:var(--card);border:1px solid var(--line);border-radius:8px;padding:14px 16px}
.stat-box b{display:block;font-family:Poppins,sans-serif;font-size:20px;font-weight:600;color:var(--orange);margin-top:8px}
.stat-box span{font-size:8px;color:var(--muted)}

/* preview */
.slider{position:absolute;left:38px;width:315px}
.slider .row{display:flex;justify-content:space-between;font-size:9.5px;color:#c7cde0}
.slider .row b{color:#fff;font-weight:600;font-size:9px}
.track{height:4px;border-radius:2px;background:#2a3350;margin-top:9px}
.track i{display:block;height:4px;border-radius:2px;background:var(--orange)}
.seg{position:absolute;top:195px;height:22px;width:98px;border-radius:12px;border:1px solid var(--line);font-size:8px;color:var(--muted);display:flex;align-items:center;justify-content:center}

.quote{font-family:Poppins,sans-serif;font-size:22px;font-weight:700;color:var(--orange);line-height:1}
.avatar{width:24px;height:24px;border-radius:50%;background:var(--orange);color:#1a1204;font-size:10px;font-weight:700;display:flex;align-items:center;justify-content:center}
.person{display:flex;gap:10px;align-items:center;position:absolute;left:20px}
.person b{font-size:9.5px;display:block}
.person span{font-size:7.5px;color:var(--muted)}
.footer a{display:block;color:var(--muted);font-size:9px;text-decoration:none;margin-top:10px}
</style>
</head>
<body>
<div class="page">

<!-- HERO -->
<section class="hero">
  <div class="hero-photo" role="img" aria-label="Modern house at dusk with solar panels on the roof and a glowing cable to a wall storage unit"></div>
  <div class="abs logo" style="left:142px;top:20px">
    <div class="mark"></div>
    <div class="brand">LUNAVOLT</div>
  </div>
  <a class="abs btn btn-hero" style="left:752px;top:36px;height:42px">JETZT PV-ANLAGE KONFIGURIEREN <span class="circ"><svg width="16" height="16" viewBox="0 0 16 16"><path d="M3 8h10M9 4l4 4-4 4" stroke="#111" stroke-width="1.8" fill="none"/></svg></span></a>
  <h1 class="abs" style="left:142px;top:152px">Ihre Photovoltaikanlage – Ehrlich Kalkuliert..</h1>
  <p class="abs sub" style="left:142px;top:294px;width:380px;color:#c8cee0">Konfigurieren Sie Ihre Solaranlage in wenigen Schritten für Einfamilienhaus, Gewerbehalle oder alles dazwischen.</p>
  <ul class="abs checks" style="left:142px;top:342px">
    <li><span class="dot"><svg width="7" height="7" viewBox="0 0 8 8"><path d="M1 4l2 2 4-4" stroke="#fff" stroke-width="1.6" fill="none"/></svg></span>Ergebnis Ohne Angabe Persönlicher Daten</li>
    <li><span class="dot"><svg width="7" height="7" viewBox="0 0 8 8"><path d="M1 4l2 2 4-4" stroke="#fff" stroke-width="1.6" fill="none"/></svg></span>Für Private &amp; Gewerbliche Dächer Jeder Größe</li>
    <li><span class="dot"><svg width="7" height="7" viewBox="0 0 8 8"><path d="M1 4l2 2 4-4" stroke="#fff" stroke-width="1.6" fill="none"/></svg></span>Realistische Einschätzung Statt Lockpreise</li>
  </ul>
  <a class="abs btn btn-hero" style="left:142px;top:440px">JETZT PV-ANLAGE KONFIGURIEREN <span class="circ"><svg width="16" height="16" viewBox="0 0 16 16"><path d="M3 8h10M9 4l4 4-4 4" stroke="#111" stroke-width="1.8" fill="none"/></svg></span></a>
  <div class="abs" style="left:484px;top:440px;width:110px">
    <div class="partner">Falke EnergiePlan</div>
  </div>
  <p class="abs" style="left:142px;top:503px;font-size:11px;color:var(--muted)">Ohne Registrierung · Ohne Kontaktdaten · Kostenlos</p>
  <svg class="abs" style="left:0;top:520px" width="1200" height="120" viewBox="0 0 1200 120"><path d="M0 45 Q600 160 1200 30 L1200 120 L0 120Z" fill="var(--bg)"/><path d="M0 45 Q600 160 1200 30" stroke="var(--orange)" stroke-width="3" fill="none"/></svg>
</section>

<!-- FEATURES -->
<div class="abs eyebrow center" style="top:707px">Features</div>
<h2 class="abs center" style="top:728px">What can the solar<br>configurator do?</h2>
<p class="abs sub center" style="top:810px">All the inputs that matter — none of the noise. Get a precise, honest picture of your<br>system in three steps.</p>
<div class="card" style="left:125px;top:888px;width:306px;height:154px;padding:24px">
  <div class="icon"><svg width="12" height="12" viewBox="0 0 12 12"><rect x="2" y="1" width="8" height="10" rx="1" stroke="#f7a21b" fill="none"/><path d="M4 4h4M4 6h4M4 8h2" stroke="#f7a21b"/></svg></div>
  <h3>Real-time calculation</h3><p>Yield, payback and savings update live as you tweak modules, orientation and storage.</p></div>
<div class="card" style="left:447px;top:888px;width:306px;height:154px;padding:24px">
  <div class="icon"><svg width="12" height="12" viewBox="0 0 12 12"><path d="M6 1l4 2v3c0 3-2 4-4 5-2-1-4-2-4-5V3z" stroke="#f7a21b" fill="none"/></svg></div>
  <h3>Transparent components</h3><p>See actual brands, datasheets and warranties — no anonymous 'premium panels'.</p></div>
<div class="card" style="left:769px;top:888px;width:306px;height:154px;padding:24px">
  <div class="icon"><svg width="12" height="12" viewBox="0 0 12 12"><path d="M2 10V2M2 10h8M4 8V6M6 8V4M8 8V5" stroke="#f7a21b"/></svg></div>
  <h3>25-year forecast</h3><p>Inflation, degradation and feed-in tariffs are modelled — not hidden.</p></div>

<!-- WHY US -->
<div class="photo" style="left:125px;top:1178px;width:452px;height:452px;background:linear-gradient(160deg,#5b8fc9 0%,#3e6fa8 45%,#1d3357 75%,#13213d 100%)" role="img" aria-label="Installer in a yellow hard hat working on rooftop solar panels"></div>
<div class="card" style="left:450px;top:1505px;width:155px;height:85px;padding:14px;background:#141b2d">
  <svg width="14" height="14" viewBox="0 0 14 14"><path d="M7 1l1.8 3.8 4 .5-3 2.8.8 4L7 10l-3.6 2.1.8-4-3-2.8 4-.5z" stroke="#f7a21b" fill="none"/></svg>
  <p style="font-size:10px;font-weight:600;color:#fff;margin-top:8px;line-height:1.4">Audited by PrüfNord-certified engineers</p></div>
<div class="abs eyebrow" style="left:622px;top:1246px">Why us</div>
<h2 class="abs" style="left:622px;top:1266px">Why our configurator is<br><span class="accent">different.</span></h2>
<p class="abs sub" style="left:622px;top:1346px;width:400px;color:#b5bccf">Most online tools optimise for lead capture. We optimise for trust: clear assumptions, no hidden margins, and a price you can actually verify.</p>
<ul class="abs checks" style="left:622px;top:1404px">
  <li style="font-weight:500;font-size:10.5px;margin-bottom:14px"><span class="dot"><svg width="7" height="7" viewBox="0 0 8 8"><path d="M1 4l2 2 4-4" stroke="#fff" stroke-width="1.6" fill="none"/></svg></span>No mandatory phone calls — you stay in control</li>
  <li style="font-weight:500;font-size:10.5px;margin-bottom:14px"><span class="dot"><svg width="7" height="7" viewBox="0 0 8 8"><path d="M1 4l2 2 4-4" stroke="#fff" stroke-width="1.6" fill="none"/></svg></span>Component-level pricing visible upfront</li>
  <li style="font-weight:500;font-size:10.5px;margin-bottom:14px"><span class="dot"><svg width="7" height="7" viewBox="0 0 8 8"><path d="M1 4l2 2 4-4" stroke="#fff" stroke-width="1.6" fill="none"/></svg></span>Independent yield model based on SolarAtlas data</li>
  <li style="font-weight:500;font-size:10.5px;margin-bottom:14px"><span class="dot"><svg width="7" height="7" viewBox="0 0 8 8"><path d="M1 4l2 2 4-4" stroke="#fff" stroke-width="1.6" fill="none"/></svg></span>Comparison-ready PDF report in one click</li>
</ul>
<a class="abs btn" style="left:622px;top:1535px;height:28px;font-size:9px">Try the configurator →</a>

<!-- FOR WHOM -->
<div class="abs eyebrow center" style="top:1770px">For whom</div>
<h2 class="abs center" style="top:1792px">Who is the configurator for?</h2>
<p class="abs sub center" style="top:1838px">Whether you own a single rooftop or run a portfolio of buildings — you'll get a precise<br>answer in minutes.</p>
<div class="card" style="left:125px;top:1918px;width:226px;height:130px;padding:20px"><div class="icon"><svg width="12" height="12" viewBox="0 0 12 12"><path d="M2 6l4-4 4 4v4H2z" stroke="#f7a21b" fill="none"/></svg></div><h3 style="font-size:11px">Homeowners</h3><p style="font-size:8.5px">Find the right system for your roof and budget.</p></div>
<div class="card" style="left:366px;top:1918px;width:226px;height:130px;padding:20px"><div class="icon"><svg width="12" height="12" viewBox="0 0 12 12"><rect x="2" y="2" width="8" height="8" stroke="#f7a21b" fill="none"/><path d="M4 4h4M4 6h4" stroke="#f7a21b"/></svg></div><h3 style="font-size:11px">Businesses</h3><p style="font-size:8.5px">Cut energy costs with rooftop or carport PV.</p></div>
<div class="card" style="left:607px;top:1918px;width:226px;height:130px;padding:20px"><div class="icon"><svg width="12" height="12" viewBox="0 0 12 12"><path d="M1 10h10M2 10V6l3-2 3 2v4M8 7h3v3" stroke="#f7a21b" fill="none"/></svg></div><h3 style="font-size:11px">Agriculture</h3><p style="font-size:8.5px">Large-area systems with feed-in optimisation.</p></div>
<div class="card" style="left:848px;top:1918px;width:227px;height:130px;padding:20px"><div class="icon"><svg width="12" height="12" viewBox="0 0 12 12"><path d="M2 10V2M2 10h8M4 8V6M6 8V4M8 8V5" stroke="#f7a21b"/></svg></div><h3 style="font-size:11px">Installers</h3><p style="font-size:8.5px">Generate proposals 5× faster for your clients.</p></div>

<!-- LIVE PREVIEW -->
<div class="abs eyebrow center" style="top:2167px">Live preview</div>
<h2 class="abs center" style="top:2186px">Configure your solar system</h2>
<p class="abs sub center" style="top:2236px">Adjust the sliders. Watch the numbers move. No signup required.</p>
<div class="card" style="left:233px;top:2286px;width:730px;height:320px;background:#121a2e;box-shadow:0 0 0 6px #0f1628">
  <div class="slider" style="top:40px"><div class="row">Roof area <b>42 m²</b></div><div class="track"><i style="width:60%"></i></div></div>
  <div class="slider" style="top:83px"><div class="row">Annual consumption <b>5,200 kWh</b></div><div class="track"><i style="width:66%"></i></div></div>
  <div class="slider" style="top:126px"><div class="row">Battery storage <b>10 kWh</b></div><div class="track"><i style="width:50%"></i></div></div>
  <div class="seg" style="left:38px;border-color:var(--orange);color:var(--orange);background:#2a2210">South</div>
  <div class="seg" style="left:146px">East/West</div>
  <div class="seg" style="left:254px">Flat</div>
  <div class="card" style="left:374px;top:39px;width:318px;height:236px;background:#182038;padding:20px">
    <div class="eyebrow" style="color:var(--muted);font-size:8px">Your estimate</div>
    <div style="font-family:Poppins,sans-serif;font-size:30px;font-weight:600;color:var(--orange);margin-top:6px">€18,420</div>
    <div style="font-size:7.5px;color:var(--muted)">Including installation &amp; VAT</div>
    <div class="stat-box" style="left:20px;top:96px;width:130px;height:74px;padding:10px 12px;background:#141b2f"><svg width="10" height="10" viewBox="0 0 10 10"><circle cx="5" cy="5" r="3.5" stroke="#f7a21b" fill="none"/></svg><b style="color:#fff;font-size:16px;margin-top:2px">9.8t</b><span>CO₂ saved / yr</span></div>
    <div class="stat-box" style="left:164px;top:96px;width:130px;height:74px;padding:10px 12px;background:#141b2f"><svg width="10" height="10" viewBox="0 0 10 10"><rect x="1.5" y="1.5" width="7" height="7" stroke="#f7a21b" fill="none"/></svg><b style="color:#fff;font-size:16px;margin-top:2px">8.2y</b><span>Payback period</span></div>
    <a class="abs btn" style="left:20px;top:192px;width:276px;height:28px;justify-content:center;border-radius:5px;font-size:9px">Get full PDF report →</a>
  </div>
</div>

<!-- MODULES BAND -->
<div class="abs" style="left:0;top:2676px;width:1200px;height:370px;background:linear-gradient(90deg,#0e1424 0%,#1e2636 30%,#262f3d 55%,#2f3f2c 85%,#24352a 100%)" role="img" aria-label="Aerial view of houses and a large building with solar panels among green trees"></div>
<div class="abs" style="left:0;top:2676px;width:1200px;height:370px;background:linear-gradient(90deg,rgba(12,17,32,.2) 20%,rgba(12,17,32,.85) 32%,rgba(12,17,32,.75) 60%,rgba(12,17,32,0) 85%)"></div>
<div class="abs eyebrow" style="left:382px;top:2768px">Modules &amp; components</div>
<h2 class="abs" style="left:382px;top:2788px">You choose. We're<br>transparent.</h2>
<p class="abs sub" style="left:382px;top:2868px;width:420px;color:#c0c6d7">Compare top-tier brands side by side: Nordpanel, Heliowerk, Kaskade, Q-Lumen and more. Mix-and-match inverters and batteries with full datasheet access.</p>
<a class="abs btn" style="left:382px;top:2928px;font-size:9px">Browse modules →</a>
<a class="abs btn ghost" style="left:540px;top:2928px;font-size:9px;background:transparent">View datasheets</a>

<!-- PROCESS -->
<div class="abs eyebrow center" style="top:3097px">Process</div>
<h2 class="abs center" style="top:3115px">From input to price in minutes</h2>
<div class="card" style="left:125px;top:3196px;width:306px;height:150px;text-align:center">
  <div class="abs" style="left:118px;top:22px;width:70px;height:70px;border-radius:50%;border:1px solid var(--line);background:#161d31"><div class="icon" style="margin:20px auto"><svg width="12" height="12" viewBox="0 0 12 12"><path d="M2 6l4-4 4 4v4H2z" stroke="#f7a21b" fill="none"/></svg></div></div>
  <div class="abs avatar" style="left:173px;top:18px;width:17px;height:17px;font-size:7px">01</div>
  <h3 style="margin-top:108px;font-size:11px">Tell us about your roof</h3><p style="font-size:8.5px">Address, size, orientation — or pick on the map.</p></div>
<div class="card" style="left:447px;top:3196px;width:306px;height:150px;text-align:center">
  <div class="abs" style="left:118px;top:22px;width:70px;height:70px;border-radius:50%;border:1px solid var(--line);background:#161d31"><div class="icon" style="margin:20px auto"><svg width="12" height="12" viewBox="0 0 12 12"><rect x="2" y="1" width="8" height="10" rx="1" stroke="#f7a21b" fill="none"/><path d="M4 4h4M4 6h4M4 8h2" stroke="#f7a21b"/></svg></div></div>
  <div class="abs avatar" style="left:173px;top:18px;width:17px;height:17px;font-size:7px">02</div>
  <h3 style="margin-top:108px;font-size:11px">We calculate honestly</h3><p style="font-size:8.5px">SolarAtlas-based yield + real component pricing.</p></div>
<div class="card" style="left:769px;top:3196px;width:306px;height:150px;text-align:center">
  <div class="abs" style="left:118px;top:22px;width:70px;height:70px;border-radius:50%;border:1px solid var(--line);background:#161d31"><div class="icon" style="margin:20px auto"><svg width="12" height="12" viewBox="0 0 12 12"><path d="M6 1l4 2v3c0 3-2 4-4 5-2-1-4-2-4-5V3z" stroke="#f7a21b" fill="none"/></svg></div></div>
  <div class="abs avatar" style="left:173px;top:18px;width:17px;height:17px;font-size:7px">03</div>
  <h3 style="margin-top:108px;font-size:11px">Get a verified offer</h3><p style="font-size:8.5px">Reviewed by certified installers in 24 hours.</p></div>

<!-- SUBSIDIES -->
<div class="photo" style="left:125px;top:3500px;width:458px;height:456px;background:radial-gradient(ellipse at 60% 70%,#8a6a3a 0,#4a3620 30%,#1c1a1c 65%,#0f1119 100%)" role="img" aria-label="Hand stacking gold coins on a table"></div>
<div class="abs eyebrow" style="left:617px;top:3617px">Subsidies</div>
<h2 class="abs" style="left:617px;top:3637px">Note on funding &amp; subsidies</h2>
<p class="abs sub" style="left:617px;top:3686px;width:460px;color:#b5bccf">Federal and regional programmes can lower your investment by up to 30%. Our configurator integrates the latest schemes and shows the net price after subsidies — automatically.</p>
<div class="stat-box" style="left:617px;top:3760px;width:225px;height:92px"><svg width="12" height="12" viewBox="0 0 12 12"><rect x="1.5" y="2.5" width="9" height="7" rx="1" stroke="#f7a21b" fill="none"/></svg><b>-30%</b><span>Avg. funding rate</span></div>
<div class="stat-box" style="left:851px;top:3760px;width:225px;height:92px"><svg width="12" height="12" viewBox="0 0 12 12"><circle cx="6" cy="6" r="4.5" stroke="#f7a21b" fill="none"/><path d="M6 3.5V6l2 1" stroke="#f7a21b" fill="none"/></svg><b>24h</b><span>Eligibility check</span></div>

<!-- REVIEWS -->
<div class="abs eyebrow center" style="top:4053px">Reviews</div>
<h2 class="abs center" style="top:4073px">What our customers say</h2>
<p class="abs sub center" style="top:4120px;font-size:9px">Rankora <span class="accent" style="letter-spacing:1px">★★★★★</span> <span style="color:#fff">4.9/5</span> from 480 reviews</p>
<div class="card" style="left:125px;top:4230px;width:306px;height:174px;padding:20px">
  <div class="quote">“</div><p style="color:#e4e8f2;font-size:9.5px;margin-top:6px">"Finally a tool that doesn't try to sell me anything. The price was within €200 of the actual installer quote."</p>
  <div class="person" style="top:110px"><div class="avatar">L</div><div><b>Lukas M.</b><span>Homeowner, Munich</span></div></div></div>
<div class="card" style="left:447px;top:4230px;width:306px;height:174px;padding:20px">
  <div class="quote">“</div><p style="color:#e4e8f2;font-size:9.5px;margin-top:6px">"Got a clear, written quote in 10 minutes. Saved me hours of back-and-forth with sales reps."</p>
  <div class="person" style="top:92px"><div class="avatar">S</div><div><b>Sandra K.</b><span>Bakery owner</span></div></div></div>
<div class="card" style="left:769px;top:4230px;width:306px;height:174px;padding:20px">
  <div class="quote">“</div><p style="color:#e4e8f2;font-size:9.5px;margin-top:6px">"I now use Lunavolt to pre-qualify leads. My closing rate doubled."</p>
  <div class="person" style="top:92px"><div class="avatar">M</div><div><b>Markus H.</b><span>PV installer</span></div></div></div>

<!-- CTA -->
<div class="card" style="left:125px;top:4540px;width:950px;height:340px;border-radius:12px;background:radial-gradient(ellipse at 100% 0%,rgba(247,150,20,.35) 0,rgba(247,150,20,0) 40%),radial-gradient(ellipse at 0% 100%,rgba(247,150,20,.22) 0,rgba(247,150,20,0) 35%),#141a2b"></div>
<svg class="abs" style="left:584px;top:4603px" width="32" height="32" viewBox="0 0 32 32"><circle cx="16" cy="16" r="6" stroke="#f7a21b" stroke-width="2" fill="none"/><path d="M16 2v5M16 25v5M2 16h5M25 16h5M6 6l3.5 3.5M22.5 22.5L26 26M6 26l3.5-3.5M22.5 9.5L26 6" stroke="#f7a21b" stroke-width="2"/></svg>
<h2 class="abs center" style="top:4652px;font-size:38px">Solar is an investment for<br><span class="accent">decades.</span></h2>
<p class="abs sub center" style="top:4752px">Make sure you start it with the right numbers. Try Lunavolt now — free,<br>no signup required.</p>
<a class="abs btn" style="left:441px;top:4818px;height:36px;padding:0 26px;font-size:10px">Start configurator →</a>
<a class="abs btn ghost" style="left:620px;top:4818px;height:36px;padding:0 24px;font-size:10px;background:#10172a">Talk to an expert</a>

<!-- FOOTER -->
<div class="abs" style="left:0;top:4978px;width:1200px;height:1px;background:var(--line)"></div>
<div class="abs" style="left:125px;top:4995px;display:flex;align-items:center;gap:16px">
  <div style="display:flex;align-items:center;gap:6px"><span style="width:16px;height:16px;border-radius:50%;border:2px solid #fff;display:inline-block"></span><span style="font-family:Poppins,sans-serif;font-size:11px;font-weight:600;color:#4fb4ff">LUNAVOLT</span></div>
  <span style="font-family:Poppins,sans-serif;font-size:11px;font-weight:700;color:#4fb4ff">Falke EnergiePlan</span>
</div>
<p class="abs sub" style="left:125px;top:5040px;width:240px;font-size:8.5px">Honest, transparent solar configuration. Built independently, free to use, no hidden agenda.</p>
<div class="abs footer" style="left:614px;top:5004px"><b style="font-family:Poppins,sans-serif;font-size:10px">Product</b><a>Configurator</a><a>Modules</a><a>Subsidies</a></div>
<div class="abs footer" style="left:858px;top:5004px"><b style="font-family:Poppins,sans-serif;font-size:10px">Company</b><a>About</a><a>Imprint</a><a>Privacy</a></div>
<div class="abs" style="left:0;top:5128px;width:1200px;height:1px;background:var(--line)"></div>
<p class="abs" style="left:125px;top:5143px;font-size:7.5px;color:var(--muted)">© 2026 Lunavolt. All rights reserved.</p>
<p class="abs" style="left:980px;top:5143px;font-size:7.5px;color:var(--muted)">Made with sunshine <span class="accent">●</span></p>

</div>
</body>
</html>
```